we need a design for Water Bottle Lable Wrap
The product is called Calmora Springs is a restructured water. its a very healthy and rejuvenating water
we were looking at using as a tag ling Restore, Recover, Rejuvenate.

```html
<!DOCTYPE html>
<html lang="en">
<head>
<meta charset="utf-8">
<title>Calmora Springs – Bottle Label Wrap</title>
<link href="https://fonts.googleapis.com/css2?family=Rubik:wght@500;600;800&display=swap" rel="stylesheet">
<style>
  :root {
    --page: #ffffff;
    --sky-top: #d6ebf5;
    --sky-mid: #bfe0ef;
    --water-low: #7cc0df;
    --water-deep: #4aa6d2;
    --ice-light: #cfe8f4;
    --ice-mid: #8ec8e6;
    --ice-deep: #5fa9d6;
    --ink: #24539a;
    --ink-soft: #3468ad;
  }
  * { box-sizing: border-box; margin: 0; padding: 0; }
  html, body {
    width: 1200px; height: 1138px; overflow: hidden;
    background: var(--page);
  }
  .label-wrap {
    position: absolute; left: 100px; top: 32px;
    width: 1000px; height: 1074px;
    background: linear-gradient(180deg, var(--sky-top) 0%, var(--sky-mid) 45%, var(--water-low) 80%, var(--water-deep) 100%);
    overflow: hidden;
    font-family: "Rubik", sans-serif;
    color: var(--ink);
    text-align: center;
  }
  .mountain-scene {
    position: absolute; left: 0; top: 350px; width: 1000px; height: 430px;
    background:
      radial-gradient(ellipse 30% 55% at 26% 45%, var(--ice-mid) 0%, transparent 70%),
      radial-gradient(ellipse 28% 60% at 74% 42%, var(--ice-mid) 0%, transparent 70%),
      radial-gradient(ellipse 60% 40% at 50% 75%, var(--ice-light) 0%, transparent 75%),
      radial-gradient(ellipse 20% 40% at 96% 55%, var(--ice-deep) 0%, transparent 70%);
    opacity: 0.85;
  }
  .brand-name {
    position: absolute; left: 0; right: 0; top: 232px;
    font-weight: 800; font-size: 136px; line-height: 148px;
    letter-spacing: -1px; text-transform: uppercase;
  }
  .divider {
    position: absolute; left: 262px; top: 523px;
    width: 490px; height: 4px; background: var(--ink);
  }
  .product-type {
    position: absolute; left: 0; right: 0; top: 540px;
    font-weight: 600; font-size: 46px; line-height: 56px;
    color: var(--ink-soft); text-transform: uppercase;
  }
  .tagline {
    position: absolute; left: 0; right: 0; top: 760px;
    font-weight: 500; font-size: 34px; line-height: 50px;
    text-transform: uppercase; letter-spacing: 0.5px;
  }
  .tagline .item { white-space: nowrap; margin: 0 4px; }
  .tick { width: 26px; height: 22px; vertical-align: -1px; margin-right: 6px; }
</style>
</head>
<body>
  <main class="label-wrap">
    <div class="mountain-scene" role="img" aria-label="Soft misty illustration of icy blue mountain peaks"></div>

    <h1 class="brand-name">Calmora<br>Springs</h1>
    <div class="divider"></div>
    <p class="product-type">Restructured<br>Water</p>

    <p class="tagline">
      <span class="item"><svg class="tick" viewBox="0 0 26 22"><path d="M2 12 L9 19 L24 3" fill="none" stroke="currentColor" stroke-width="4" stroke-linecap="round" stroke-linejoin="round"/></svg>Restore</span>
      <span class="item"><svg class="tick" viewBox="0 0 26 22"><path d="M2 12 L9 19 L24 3" fill="none" stroke="currentColor" stroke-width="4" stroke-linecap="round" stroke-linejoin="round"/></svg>Recover</span><br>
      <span class="item"><svg class="tick" viewBox="0 0 26 22"><path d="M2 12 L9 19 L24 3" fill="none" stroke="currentColor" stroke-width="4" stroke-linecap="round" stroke-linejoin="round"/></svg>Rejuvenate</span>
    </p>
  </main>
</body>
</html>
```